Business Card Design

Hi I need a business card designed, we already have the business name logo artwork and would like some concept ideas for the Bus Card layout.
On the back of the card i want to include the products and services that we offer.
We are a Plastics Sheeting manufacture based in Perth Australia.

                                       

We need a BC design for a company called Dunrove Plastics based in Perth Australia.

We supply from DIY to Trade & Industrial  Engineering Markets.

We specialise in:

·         Cut to size panels  (all shapes and sizes)

·         Plastics fabrication & Welding

·         Custom Designs

·         Plastic Repairs

·         PVC Pipe Slotting & PVC Pipe Threading

·         Supplier of all types of engineering plastics and profiles.

Including:           Acrylic / Clarvin

                               Polycarbonate / Durok

                               Prismatic Light Diffuser

                               Tembrill

                               HDPE / UHMWPE

                               PVC / PVC Foam

                               Nylon

                               HIPS

```html
<!DOCTYPE html>
<html lang="en">
<head>
<meta charset="utf-8">
<title>Dunrove Plastics – Business Card</title>
<link href="https://fonts.googleapis.com/css2?family=Maven+Pro:wght@400;500;700&display=swap" rel="stylesheet">
<style>
  :root {
    --navy: #1c2b5a;
    --paper: #eef1f0;
    --backdrop: #e2e3e3;
    --shadow: #adaeaf;
    --light-text: #e9ecf3;
  }
  * { box-sizing: border-box; margin: 0; padding: 0; }
  html, body { width: 800px; height: 1200px; overflow: hidden; }
  body {
    background: var(--backdrop);
    font-family: "Maven Pro", sans-serif;
    position: relative;
  }
  .card {
    position: absolute;
    left: 184px;
    width: 432px;
  }
  .card--front { top: 37px; }
  .card--back { top: 310px; }
  .card__shadow {
    display: block;
    width: 432px; height: 11px;
  }
  .card__top, .card__bottom { position: relative; }
  .card__top { background: var(--paper); height: 126px; }
  .card__bottom { background: var(--navy); color: var(--light-text); height: 127px; }

  .brand {
    position: absolute; inset: 0;
    display: flex; align-items: center; justify-content: center;
    font-weight: 700; font-size: 40px; color: var(--navy);
    padding-bottom: 6px;
  }
  .holder { text-align: center; padding-top: 5px; }
  .holder__name { font-size: 22px; font-weight: 400; line-height: 26px; }
  .holder__role { font-size: 14.5px; font-weight: 400; line-height: 18px; }
  .contact {
    position: absolute; top: 57px; left: 20px; right: 20px;
    display: flex; justify-content: space-between;
    font-size: 10.3px; line-height: 14px;
  }
  .contact__address { text-align: right; }

  .offer {
    display: grid;
    grid-template-columns: 128px 1fr;
    column-gap: 10px;
    padding-top: 24px;
    font-size: 9.6px; line-height: 13.4px; font-style: italic;
  }
  .offer__label { text-align: right; font-weight: 500; }
  .offer__list { list-style: none; }
  .card__top .offer { color: var(--navy); }
  .card__bottom .offer { padding-top: 9px; }
</style>
</head>
<body>
  <section class="card card--front">
    <div class="card__top">
      <div class="brand">Dunrove Plastics</div>
    </div>
    <div class="card__bottom">
      <div class="holder">
        <p class="holder__name">Maren Talbot</p>
        <p class="holder__role">Manager</p>
      </div>
      <div class="contact">
        <div class="contact__lines">
          <p>Phone: 08 5550 2011</p>
          <p>Fax: 08 5550 2022</p>
          <p>Mobile: 0400 555 631</p>
          <p>Email: sales@dunroveplastics.com.au</p>
        </div>
        <div class="contact__address">
          <p>Unit 4/18 Harlow Circuit</p>
          <p>Kelmscott Vale WA 6112</p>
          <p>PO Box 2840 Kelmscott Vale DC WA 6991</p>
          <p>ABN: 12 345 678 901</p>
        </div>
      </div>
    </div>
    <svg class="card__shadow" viewBox="0 0 432 11" preserveAspectRatio="none" aria-hidden="true">
      <path d="M0 0 H432 V11 Q216 -3 0 11 Z" fill="var(--shadow)"/>
    </svg>
  </section>

  <section class="card card--back">
    <div class="card__top">
      <div class="offer">
        <p class="offer__label">We specialise in:</p>
        <ul class="offer__list">
          <li>Cut to size panels&nbsp; (all shapes and sizes)</li>
          <li>Plastics fabrication &amp; Welding</li>
          <li>Custom Designs</li>
          <li>Plastic Repairs</li>
          <li>PVC Pipe Slotting &amp; PVC Pipe Threading</li>
          <li>Supplier of all types of engineering plastics and profiles</li>
        </ul>
      </div>
    </div>
    <div class="card__bottom">
      <div class="offer">
        <p class="offer__label">Including:</p>
        <ul class="offer__list">
          <li>Acrylic / Clarvin</li>
          <li>Polycarbonate / Durok</li>
          <li>Prismatic Light Diffuser</li>
          <li>Tembrill</li>
          <li>HDPE / UHMWPE</li>
          <li>PVC / PVC Foam</li>
          <li>Nylon</li>
          <li>HIPS</li>
        </ul>
      </div>
    </div>
    <svg class="card__shadow" viewBox="0 0 432 11" preserveAspectRatio="none" aria-hidden="true">
      <path d="M0 0 H432 V11 Q216 -3 0 11 Z" fill="var(--shadow)"/>
    </svg>
  </section>
</body>
</html>
```